Football blog needs a Wordpress design new site

We need a wordpress design for a new football blog site. We would like to see a design that uses the colours green, white and black and one that makes good use of the slideshow widgets as scene in the site 'www.tarnwick.net'
We would like a modern and sleek looking site but one that is also professional and easy to navigate.
Unfortunately due to unforeseen circumstances we are having to shorten the deadline date for this project.
The new deadline date is 16/07/2014.
We apologise for any inconveniance
Industry/Entity Type
It Professional
Look and feel

```html
<!DOCTYPE html>
<html lang="en">
<head>
<meta charset="utf-8">
<title>Sideline Chatter – Football Blog</title>
<link rel="stylesheet" href="https://fonts.googleapis.com/css2?family=Oswald:wght@400;500;700&family=Open+Sans:wght@400;600;700&display=swap">
<style>
:root{
  --green:#3cae2c;
  --green-dark:#2e8c21;
  --black:#111111;
  --panel:#1b1b1b;
  --panel-2:#262626;
  --ink:#222222;
  --text:#555555;
  --muted:#8a8a8a;
  --line:#e4e4e4;
  --page-bg:#ececec;
  --white:#ffffff;
  --fb:#3b5a9a;
  --tw:#2fa8e0;
  --gp:#d9463a;
  --yt:#c8231c;
  --vm:#2e9fd3;
  --dr:#e24f88;
  --rss:#f08a24;
}
*{box-sizing:border-box;margin:0;padding:0}
html,body{width:1200px;height:3692px;overflow:hidden}
body{position:relative;background:var(--page-bg);font-family:'Open Sans',sans-serif;color:var(--text);font-size:11px;line-height:1.45}
ul{list-style:none}

/* image placeholders */
.ph{display:block;background:linear-gradient(135deg,#2d4b2a 0%,#5f8a3a 55%,#b9b08a 100%)}
.ph.red{background:linear-gradient(135deg,#5a1b1b 0%,#a23a2a 50%,#3f6a2c 100%)}
.ph.blue{background:linear-gradient(135deg,#1e3656 0%,#3f6f9c 50%,#5f8a3a 100%)}
.ph.night{background:linear-gradient(160deg,#141d2c 0%,#2f4a38 60%,#6e8d4a 100%)}
.ph.crowd{background:linear-gradient(135deg,#3b2a22 0%,#8a5a3a 50%,#c9a36a 100%)}
.ph.ad-top{background:linear-gradient(90deg,#0f3b1e 0%,#1f7a33 45%,#e4c21f 100%)}
.ph.ad-host-fill{background:linear-gradient(180deg,#6fc3ef 0%,#2f86c9 55%,#f2d23a 100%)}
.ph.ad-niche-fill{background:linear-gradient(180deg,#f3c23a 0%,#2a5ea8 50%,#d9463a 100%)}

/* page frame */
.page{position:absolute;left:160px;top:44px;width:880px;height:3640px;background:var(--white);padding:0 14px}

.topbar{height:38px;display:flex;justify-content:space-between;align-items:center;border-bottom:1px solid var(--line)}
.topbar-links{display:flex}
.topbar-links a{color:var(--muted);text-decoration:none;font-size:11px;padding:0 10px;border-right:1px solid var(--line)}
.topbar-links a:first-child{padding-left:0}
.follow{display:flex;align-items:center;gap:5px;font-size:11px;color:var(--muted)}
.follow span.sq{width:16px;height:16px;display:block}

.masthead{height:76px;display:flex;justify-content:space-between;align-items:center}
.brand{display:flex;align-items:center;gap:10px}
.brand-dot{width:40px;height:40px;border-radius:50%;background:var(--green)}
.brand-name{font-family:'Oswald',sans-serif;font-weight:500;font-size:32px;color:var(--black);letter-spacing:.3px}
.banner{width:346px;height:42px}

.mainnav{height:36px;background:var(--black);display:flex;align-items:stretch;justify-content:space-between}
.mainnav ul{display:flex}
.mainnav li a{display:flex;align-items:center;height:36px;padding:0 16px;color:var(--white);text-decoration:none;font-family:'Oswald',sans-serif;font-size:13px;letter-spacing:.4px}
.mainnav li.active a{background:var(--green)}
.search{width:36px;background:#333;display:flex;align-items:center;justify-content:center}

/* slider */
.slider{margin-top:12px;height:332px;display:flex;background:var(--panel)}
.slide-main{position:relative;width:576px;height:332px}
.slide-main .ph{position:absolute;inset:0}
.caption{position:absolute;left:0;right:0;bottom:0;background:rgba(15,15,15,.88);display:flex;align-items:center;gap:12px;padding:10px 14px}
.caption .ico{width:36px;height:36px;border-radius:50%;border:2px solid var(--white);flex:none;display:flex;align-items:center;justify-content:center}
.caption .ico::after{content:"";width:10px;height:10px;border-radius:50%;background:var(--green)}
.cat{display:block;color:#cfcfcf;font-size:9px}
.caption h3{font-family:'Oswald',sans-serif;font-weight:500;color:var(--green);font-size:19px;line-height:1.2;text-transform:uppercase}
.caption time{display:block;color:#bdbdbd;font-size:9px}
.slide-list{flex:1;padding:4px 10px}
.slide-list li{display:flex;gap:10px;height:81px;align-items:center;border-bottom:1px solid #333}
.slide-list li:last-child{border-bottom:0}
.slide-list .ph{width:62px;height:56px;flex:none}
.slide-list h4{font-family:'Oswald',sans-serif;font-weight:400;font-size:11px;color:var(--white);line-height:1.35;text-transform:uppercase}
.slide-list time{font-size:9px;color:#aaa}
.slide-list .tag{font-size:9px;color:var(--green);margin-left:8px}

/* section heads */
.section-head{height:40px;margin-bottom:16px;display:flex;align-items:center;gap:12px}
.section-head h2{font-family:'Oswald',sans-serif;font-weight:500;font-size:19px;color:var(--black);text-transform:uppercase;white-space:nowrap}
.section-head::after{content:"";flex:1;height:3px;background:#ececec}

.meta{font-size:9px;color:var(--muted);display:flex;gap:12px;align-items:center}
.meta span{display:inline-flex;align-items:center;gap:4px}
.meta span::before{content:"";width:7px;height:7px;border:1px solid #aaa;border-radius:50%}

/* latest news */
.latest{margin-top:18px;height:230px;margin-bottom:14px}
.card-row{display:grid;grid-template-columns:repeat(4,198px);gap:20px}
.card .ph{height:108px}
.card h3{margin-top:10px;font-family:'Oswald',sans-serif;font-weight:500;font-size:11px;color:var(--ink);text-transform:uppercase}
.card.hl h3{color:var(--green)}
.card .meta{margin-top:4px}

.columns{display:flex;gap:54px}
.main-col{width:566px}
.side-col{width:232px}

/* competitions */
.competitions{height:386px;margin-bottom:24px}
.comp-body{display:flex;gap:18px}
.comp-feature{width:355px}
.comp-feature .ph{height:190px}
.comp-feature .meta{margin-top:12px}
.comp-feature p{margin-top:10px;font-size:10.5px;line-height:1.55}
.btn{display:inline-block;margin-top:14px;background:var(--green);color:var(--white);font-family:'Oswald',sans-serif;font-size:10px;padding:5px 10px;text-decoration:none;text-transform:uppercase}
.comp-list{flex:1}
.comp-list li{margin-bottom:22px}
.comp-list h4{font-family:'Oswald',sans-serif;font-weight:500;font-size:11.5px;color:var(--ink);line-height:1.4;text-transform:uppercase}
.comp-list li.hl h4{color:var(--green)}
.comp-list .meta{margin-top:5px}

/* pictures */
.pictures{height:346px;margin-bottom:26px}
.gallery{height:290px;background:var(--panel);display:flex;gap:4px;padding:4px}
.gallery-main{position:relative;width:278px;height:282px}
.gallery-main .ph{position:absolute;inset:0}
.gallery-main .caption h3{font-size:14px}
.gallery-grid{flex:1;display:grid;grid-template-columns:repeat(3,1fr);grid-template-rows:repeat(3,1fr);gap:4px}

/* world cup */
.worldcup{height:368px;margin-bottom:66px}
.wc-grid{display:grid;grid-template-columns:repeat(4,127px);column-gap:19px;row-gap:20px}
.wc-card{height:146px}
.wc-card .ph{height:76px}
.wc-card h3{margin-top:8px;font-family:'Oswald',sans-serif;font-weight:500;font-size:10.5px;color:var(--ink);text-transform:uppercase}
.wc-card.hl h3{color:var(--green)}
.wc-card p{margin-top:3px;font-size:9.5px;line-height:1.5}

/* videos */
.videos{height:342px;margin-bottom:34px}
.video-frame{height:286px;background:var(--panel);display:flex;gap:6px;padding:6px}
.video-main{position:relative;width:400px}
.video-main .ph,.video-thumb .ph{position:absolute;inset:0}
.video-side{flex:1;display:flex;flex-direction:column;gap:6px}
.video-thumb{position:relative;flex:1}
.play{position:absolute;left:50%;top:50%;transform:translate(-50%,-50%)}

/* blog */
.blog-list li{display:flex;gap:16px;height:124px;margin-bottom:39px}
.blog-list .ph{width:188px;height:124px;flex:none}
.blog-list h3{font-family:'Oswald',sans-serif;font-weight:500;font-size:12.5px;color:var(--ink);text-transform:uppercase;margin-top:4px}
.blog-list .by{font-size:9px;color:var(--muted);margin-top:4px}
.blog-list .by b{color:var(--green);font-weight:600}
.blog-list p{margin-top:6px;font-size:10px;line-height:1.55}
.share{display:flex;gap:6px;margin-top:8px}
.share i{width:12px;height:12px;display:block}

/* sidebar */
.social-grid{margin-top:25px;display:grid;grid-template-columns:repeat(3,1fr);gap:10px}
.social-tile{height:64px;color:var(--white);display:flex;flex-direction:column;align-items:center;justify-content:center;gap:2px}
.social-tile b{font-size:12px;font-weight:700}
.social-tile small{font-size:9px;opacity:.9}
.t-fb{background:var(--fb)}.t-tw{background:var(--tw)}.t-gp{background:var(--gp)}
.t-yt{background:var(--yt)}.t-vm{background:var(--vm)}.t-dr{background:var(--dr)}
.players{margin-top:31px}
.players .section-head{margin-bottom:6px}
.player-list li{display:flex;gap:10px;height:58px;margin-bottom:10px;align-items:flex-start}
.player-list .ph{width:52px;height:46px;flex:none}
.player-list h4{font-family:'Oswald',sans-serif;font-weight:400;font-size:11px;color:var(--ink);text-transform:uppercase;line-height:1.35}
.player-list time{font-size:9px;color:var(--muted)}
.ad-host{margin-top:29px;height:231px}
.popular{margin-top:49px}
.popular .section-head{margin-bottom:3px}
.pop-card{position:relative;height:170px;margin-bottom:13px}
.pop-card .ph{position:absolute;inset:0}
.pop-card .caption{padding:8px 10px;gap:8px}
.pop-card .caption .ico{width:28px;height:28px}
.pop-card .caption h3{font-size:11px;color:var(--white)}
.ad-niche{margin-top:37px;height:323px}

/* footer */
.site-footer{position:absolute;left:0;right:0;bottom:0;height:413px;background:var(--black)}
.footer-cols{height:375px;display:flex;gap:40px;padding:22px 14px 0}
.footer-cols > div{flex:1}
.footer-cols h2{font-family:'Oswald',sans-serif;font-weight:500;font-size:16px;color:var(--white);text-transform:uppercase;margin-bottom:16px}
.footer-cols p{color:#9a9a9a;font-size:10px;line-height:1.6}
.foot-social{margin-top:18px;display:grid;grid-template-columns:repeat(3,60px);gap:8px}
.foot-social .social-tile{height:56px}
.reviews li{display:flex;gap:10px;margin-bottom:14px}
.reviews .ph{width:52px;height:44px;flex:none}
.reviews h4{font-family:'Oswald',sans-serif;font-weight:400;font-size:11px;color:var(--white);text-transform:uppercase;line-height:1.35}
.reviews time{font-size:9px;color:#888}
.field{display:block;margin-top:12px;height:28px;background:#222;border:1px solid #333;color:#888;font-size:10px;padding:0 10px;line-height:26px}
.subscribe{display:block;margin-top:12px;height:30px;background:var(--green);color:var(--white);text-align:center;line-height:30px;font-family:'Oswald',sans-serif;font-size:12px;text-transform:uppercase}
.bottombar{height:38px;background:#0a0a0a;border-top:1px solid #222;display:flex;justify-content:space-between;align-items:center;padding:0 14px;font-size:9.5px;color:#888}
.bottombar nav{display:flex;gap:18px}
</style>
</head>
<body>
<div class="page">

  <header>
    <div class="topbar">
      <nav class="topbar-links"><a href="#">Home</a><a href="#">About Us</a><a href="#">Advertising</a><a href="#">Contact Us</a></nav>
      <div class="follow">Follow <span class="sq t-fb"></span><span class="sq t-tw"></span><span class="sq t-gp"></span><span class="sq t-yt"></span></div>
    </div>
    <div class="masthead">
      <div class="brand"><span class="brand-dot"></span><span class="brand-name">Sideline Chatter</span></div>
      <div class="banner ph ad-top" role="img" aria-label="Football promotion banner advertisement"></div>
    </div>
    <nav class="mainnav">
      <ul>
        <li class="active"><a href="#">HOME</a></li>
        <li><a href="#">SIDELINE BLOG</a></li>
        <li><a href="#">WORLD CUP</a></li>
        <li><a href="#">LATEST NEWS</a></li>
        <li><a href="#">VIDEO</a></li>
        <li><a href="#">PLAYERS</a></li>
        <li><a href="#">COMPETITIONS</a></li>
      </ul>
      <div class="search"><svg width="14" height="14" viewBox="0 0 14 14"><circle cx="6" cy="6" r="4.5" fill="none" stroke="#fff" stroke-width="1.8"/><line x1="9.3" y1="9.3" x2="13" y2="13" stroke="#fff" stroke-width="1.8"/></svg></div>
    </nav>
  </header>

  <section class="slider">
    <div class="slide-main">
      <div class="ph night" role="img" aria-label="Two players challenging for the ball in a night match"></div>
      <div class="caption"><span class="ico"></span><div><span class="cat">Reviews</span><h3>Lorem ipsum is simply dummy text of the...</h3><time>July 10, 2014 · Players</time></div></div>
    </div>
    <ul class="slide-list">
      <li><span class="ph red" role="img" aria-label="Match action photo"></span><div><h4>Lorem ipsum is simply dummy text of the printing</h4><time>July 10, 2014</time><span class="tag">Players</span></div></li>
      <li><span class="ph blue" role="img" aria-label="Match action photo"></span><div><h4>Lorem ipsum is simply dummy text of the printing</h4><time>July 10, 2014</time><span class="tag">Players</span></div></li>
      <li><span class="ph crowd" role="img" aria-label="Match action photo"></span><div><h4>Lorem ipsum is simply dummy text of the printing</h4><time>July 10, 2014</time><span class="tag">Players</span></div></li>
      <li><span class="ph" role="img" aria-label="Match action photo"></span><div><h4>Lorem ipsum is simply dummy text of the printing</h4><time>July 10, 2014</time><span class="tag">Players</span></div></li>
    </ul>
  </section>

  <section class="latest">
    <div class="section-head"><h2>Latest News</h2></div>
    <div class="card-row">
      <article class="card hl"><span class="ph red" role="img" aria-label="Players in red kits on the pitch"></span><h3>Lorem ipsum is simply</h3><div class="meta"><span>July 10, 2014</span></div></article>
      <article class="card"><span class="ph night" role="img" aria-label="Stadium under floodlights"></span><h3>Lorem ipsum is simply</h3><div class="meta"><span>July 10, 2014</span></div></article>
      <article class="card"><span class="ph crowd" role="img" aria-label="Player shooting at goal"></span><h3>Lorem ipsum is simply</h3><div class="meta"><span>July 10, 2014</span></div></article>
      <article class="card"><span class="ph blue" role="img" aria-label="Player celebrating a goal"></span><h3>Lorem ipsum is simply</h3><div class="meta"><span>July 10, 2014</span></div></article>
    </div>
  </section>

  <div class="columns">
    <main class="main-col">

      <section class="competitions">
        <div class="section-head"><h2>Competitions</h2></div>
        <div class="comp-body">
          <article class="comp-feature">
            <span class="ph" role="img" aria-label="Boot striking a football on grass"></span>
            <div class="meta"><span>July 10, 2014</span><span>Blog Category</span><span>0 Comments</span></div>
            <p>Lorem Ipsum is simply dummy text of the printing and typesetting. Buy industry Lorem Ipsum has been the standard dummy text ever since.</p>
            <a class="btn" href="#">Read more</a>
          </article>
          <ul class="comp-list">
            <li class="hl"><h4>Lorem ipsum is simply text of the and typesetting</h4><div class="meta"><span>July 10, 2014</span><span>0</span></div></li>
            <li><h4>Lorem ipsum is simply text of the typesetting</h4><div class="meta"><span>July 10, 2014</span><span>0</span></div></li>
            <li><h4>Lorem ipsum is simply text of the typesetting</h4><div class="meta"><span>July 10, 2014</span><span>0</span></div></li>
            <li><h4>Lorem ipsum is simply text of the typesetting</h4><div class="meta"><span>July 10, 2014</span><span>0</span></div></li>
          </ul>
        </div>
      </section>

      <section class="pictures">
        <div class="section-head"><h2>News in Pictures</h2></div>
        <div class="gallery">
          <div class="gallery-main">
            <div class="ph blue" role="img" aria-label="Goalkeeper diving for the ball"></div>
            <div class="caption"><span class="ico"></span><div><h3>Lorem ipsum is text of the...</h3><time>July 10, 2014</time></div></div>
          </div>
          <div class="gallery-grid">
            <span class="ph" role="img" aria-label="Pitch seen from above"></span>
            <span class="ph red" role="img" aria-label="Players in a tackle"></span>
            <span class="ph night" role="img" aria-label="Stadium at night"></span>
            <span class="ph crowd" role="img" aria-label="Fans in the stands"></span>
            <span class="ph blue" role="img" aria-label="Team lining up"></span>
            <span class="ph" role="img" aria-label="Ball in the net"></span>
            <span class="ph red" role="img" aria-label="Player dribbling"></span>
            <span class="ph crowd" role="img" aria-label="Coach on the touchline"></span>
            <span class="ph night" role="img" aria-label="Corner kick"></span>
          </div>
        </div>
      </section>

      <section class="worldcup">
        <div class="section-head"><h2>World Cup</h2></div>
        <div class="wc-grid">
          <article class="wc-card hl"><span class="ph red" role="img" aria-label="Match photo"></span><h3>Lorem ipsum is simply</h3><p>Lorem ipsum is simply dummy text of the printing and type.</p></article>
          <article class="wc-card"><span class="ph crowd" role="img" aria-label="Match photo"></span><h3>Lorem ipsum is simply</h3><p>Dummy text of the printing and typesetting industry.</p></article>
          <article class="wc-card"><span class="ph night" role="img" aria-label="Match photo"></span><h3>Lorem ipsum is simply</h3><p>Dummy text of the printing and typesetting industry.</p></article>
          <article class="wc-card"><span class="ph blue" role="img" aria-label="Match photo"></span><h3>Lorem ipsum is simply</h3><p>Dummy text of the printing and typesetting industry.</p></article>
          <article class="wc-card hl"><span class="ph" role="img" aria-label="Match photo"></span><h3>Lorem ipsum is simply</h3><p>Lorem ipsum is simply dummy text of the printing and type.</p></article>
          <article class="wc-card"><span class="ph red" role="img" aria-label="Match photo"></span><h3>Lorem ipsum is simply</h3><p>Lorem ipsum is simply dummy text of the printing and type.</p></article>
          <article class="wc-card"><span class="ph crowd" role="img" aria-label="Match photo"></span><h3>Lorem ipsum is simply</h3><p>Lorem ipsum is simply dummy text of the printing and type.</p></article>
          <article class="wc-card"><span class="ph night" role="img" aria-label="Match photo"></span><h3>Lorem ipsum is simply</h3><p>Lorem ipsum is simply dummy text of the printing and type.</p></article>
        </div>
      </section>

      <section class="videos">
        <div class="section-head"><h2>Top Videos</h2></div>
        <div class="video-frame">
          <div class="video-main">
            <div class="ph night" role="img" aria-label="Video still of two players chasing the ball"></div>
            <svg class="play" width="54" height="54" viewBox="0 0 54 54"><circle cx="27" cy="27" r="25" fill="rgba(0,0,0,.45)" stroke="#fff" stroke-width="2"/><path d="M22 17 L37 27 L22 37 Z" fill="#fff"/></svg>
          </div>
          <div class="video-side">
            <div class="video-thumb"><div class="ph red" role="img" aria-label="Video still of a match"></div><svg class="play" width="34" height="34" viewBox="0 0 54 54"><circle cx="27" cy="27" r="25" fill="rgba(0,0,0,.45)" stroke="#fff" stroke-width="2"/><path d="M22 17 L37 27 L22 37 Z" fill="#fff"/></svg></div>
            <div class="video-thumb"><div class="ph" role="img" aria-label="Video still of a match"></div><svg class="play" width="34" height="34" viewBox="0 0 54 54"><circle cx="27" cy="27" r="25" fill="rgba(0,0,0,.45)" stroke="#fff" stroke-width="2"/><path d="M22 17 L37 27 L22 37 Z" fill="#fff"/></svg></div>
          </div>
        </div>
      </section>

      <section class="blog">
        <div class="section-head"><h2>Sideline Blog</h2></div>
        <ul class="blog-list">
          <li><span class="ph red" role="img" aria-label="Blog post photo"></span><div><h3>Lorem ipsum dolor sit amet, consectetur adipisicing</h3><div class="by"><b>July 10, 2014</b> · By Lorem Ipsum</div><p>Lorem ipsum dolor sit amet, consectetur adipisicing elit, sed do eiusmod tempor incididunt ut labore et dolore magna aliqua. Ut enim ad minim veniam.</p><div class="share"><i class="t-fb"></i><i class="t-tw"></i><i class="t-gp"></i><i style="background:var(--rss)"></i></div></div></li>
          <li><span class="ph night" role="img" aria-label="Blog post photo"></span><div><h3>Lorem ipsum dolor sit amet, consectetur adipisicing</h3><div class="by"><b>July 10, 2014</b> · By Lorem Ipsum</div><p>Lorem ipsum dolor sit amet, consectetur adipisicing elit, sed do eiusmod tempor incididunt ut labore et dolore magna aliqua. Ut enim ad minim veniam.</p><div class="share"><i class="t-fb"></i><i class="t-tw"></i><i class="t-gp"></i><i style="background:var(--rss)"></i></div></div></li>
          <li><span class="ph crowd" role="img" aria-label="Blog post photo"></span><div><h3>Lorem ipsum dolor sit amet, consectetur adipisicing</h3><div class="by"><b>July 10, 2014</b> · By Lorem Ipsum</div><p>Lorem ipsum dolor sit amet, consectetur adipisicing elit, sed do eiusmod tempor incididunt ut labore et dolore magna aliqua. Ut enim ad minim veniam.</p><div class="share"><i class="t-fb"></i><i class="t-tw"></i><i class="t-gp"></i><i style="background:var(--rss)"></i></div></div></li>
          <li><span class="ph blue" role="img" aria-label="Blog post photo"></span><div><h3>Lorem ipsum dolor sit amet, consectetur adipisicing</h3><div class="by"><b>July 10, 2014</b> · By Lorem Ipsum</div><p>Lorem ipsum dolor sit amet, consectetur adipisicing elit, sed do eiusmod tempor incididunt ut labore et dolore magna aliqua. Ut enim ad minim veniam.</p><div class="share"><i class="t-fb"></i><i class="t-tw"></i><i class="t-gp"></i><i style="background:var(--rss)"></i></div></div></li>
          <li><span class="ph" role="img" aria-label="Blog post photo"></span><div><h3>Lorem ipsum dolor sit amet, consectetur adipisicing</h3><div class="by"><b>July 10, 2014</b> · By Lorem Ipsum</div><p>Lorem ipsum dolor sit amet, consectetur adipisicing elit, sed do eiusmod tempor incididunt ut labore et dolore magna aliqua. Ut enim ad minim veniam.</p><div class="share"><i class="t-fb"></i><i class="t-tw"></i><i class="t-gp"></i><i style="background:var(--rss)"></i></div></div></li>
        </ul>
      </section>
    </main>

    <aside class="side-col">
      <div class="social-grid">
        <div class="social-tile t-fb"><b>40,345</b><small>Fans</small></div>
        <div class="social-tile t-tw"><b>3,241</b><small>Followers</small></div>
        <div class="social-tile t-gp"><b>1,208</b><small>Followers</small></div>
        <div class="social-tile t-yt"><b>5,980</b><small>Subscribers</small></div>
        <div class="social-tile t-vm"><b>2,110</b><small>Followers</small></div>
        <div class="social-tile t-dr"><b>9,650</b><small>Followers</small></div>
      </div>

      <section class="players">
        <div class="section-head"><h2>Players</h2></div>
        <ul class="player-list">
          <li><span class="ph red" role="img" aria-label="Player photo"></span><div><h4>Lorem ipsum is simply dummy text of the</h4><time>July 10, 2014</time></div></li>
          <li><span class="ph blue" role="img" aria-label="Player photo"></span><div><h4>Lorem ipsum is simply dummy text of the</h4><time>July 10, 2014</time></div></li>
          <li><span class="ph crowd" role="img" aria-label="Player photo"></span><div><h4>Lorem ipsum is simply dummy text of the</h4><time>July 10, 2014</time></div></li>
          <li><span class="ph night" role="img" aria-label="Player photo"></span><div><h4>Lorem ipsum dummy text of the printing</h4><time>July 10, 2014</time></div></li>
          <li><span class="ph" role="img" aria-label="Player photo"></span><div><h4>Lorem ipsum is simply dummy text of the</h4><time>July 10, 2014</time></div></li>
          <li><span class="ph red" role="img" aria-label="Player photo"></span><div><h4>Lorem ipsum simply text of the printing</h4><time>July 10, 2014</time></div></li>
        </ul>
      </section>

      <div class="ad-host ph ad-host-fill" role="img" aria-label="Web hosting advertisement"></div>

      <section class="popular">
        <div class="section-head"><h2>Most Popular</h2></div>
        <article class="pop-card"><div class="ph red" role="img" aria-label="Popular story photo"></div><div class="caption"><span class="ico"></span><div><span class="cat">Reviews</span><h3>Lorem ipsum is simply dummy text</h3><time>July 10, 2014</time></div></div></article>
        <article class="pop-card"><div class="ph crowd" role="img" aria-label="Popular story photo"></div><div class="caption"><span class="ico"></span><div><span class="cat">Reviews</span><h3>Lorem ipsum is simply dummy text</h3><time>July 10, 2014</time></div></div></article>
        <article class="pop-card"><div class="ph blue" role="img" aria-label="Popular story photo"></div><div class="caption"><span class="ico"></span><div><span class="cat">Reviews</span><h3>Lorem ipsum is simply dummy text</h3><time>July 10, 2014</time></div></div></article>
        <article class="pop-card"><div class="ph night" role="img" aria-label="Popular story photo"></div><div class="caption"><span class="ico"></span><div><span class="cat">Reviews</span><h3>Lorem ipsum is simply dummy text</h3><time>July 10, 2014</time></div></div></article>
      </section>

      <div class="ad-niche ph ad-niche-fill" role="img" aria-label="Keyword research tool advertisement"></div>
    </aside>
  </div>

  <footer class="site-footer">
    <div class="footer-cols">
      <div>
        <h2>Sideline Chatter</h2>
        <p>Lorem ipsum dolor sit amet, consectetur adipisicing elit, sed do eiusmod tempor incididunt ut labore et dolore magna aliqua.</p>
        <div class="foot-social">
          <div class="social-tile t-fb"><b>40,345</b></div>
          <div class="social-tile t-tw"><b>3,241</b></div>
          <div class="social-tile t-gp"><b>1,208</b></div>
          <div class="social-tile t-yt"><b>5,980</b></div>
          <div class="social-tile t-vm"><b>2,110</b></div>
          <div class="social-tile t-dr"><b>9,650</b></div>
        </div>
      </div>
      <div>
        <h2>Best Reviews</h2>
        <ul class="reviews">
          <li><span class="ph red" role="img" aria-label="Review photo"></span><div><h4>Lorem ipsum is simply dummy text of the</h4><time>July 10, 2014</time></div></li>
          <li><span class="ph blue" role="img" aria-label="Review photo"></span><div><h4>Lorem ipsum is simply dummy text of the</h4><time>July 10, 2014</time></div></li>
          <li><span class="ph crowd" role="img" aria-label="Review photo"></span><div><h4>Lorem ipsum is simply dummy text of the</h4><time>July 10, 2014</time></div></li>
        </ul>
      </div>
      <div>
        <h2>Weekly Newsletter</h2>
        <p>Lorem ipsum dolor sit amet, consectetur adipisicing elit, sed do eiusmod tempor incididunt ut labore et dolore magna aliqua.</p>
        <span class="field">Your name</span>
        <span class="field">Your email</span>
        <span class="subscribe">Subscribe</span>
      </div>
    </div>
    <div class="bottombar">
      <span>© Copyright 2014 Sideline Chatter</span>
      <nav><span>Home</span><span>Sideline Blog</span><span>World Cup</span><span>Top News</span><span>Media</span><span>Competitions</span></nav>
    </div>
  </footer>
</div>
</body>
</html>
```